Commercial photographer, UAV drone photography & 360 walk-through visuals

I need a business card design that is minimalist but yet pretentiously creative. My target market are architects, designers, advertising agents and marketing managers. It is important to stress that though I am asking for a minimalist design it needs to have creative impact.

Target Market(s)

Architects, interiors designers, web-designers, artists

Contact Information for Business Card

Include my name, mobile [cell] number, email, web page and the company logo. Do not to include a postal address.

Colors

Designer to choose colors to be used in the design.

Requirements
Must have
• The following information is to be included:
• Miles Perrow
• Photographer
• m: 07812 593174
• e: miles@mpframeworks.co.uk
• w: mpframeworks.co.uk

```html
<!DOCTYPE html>
<html lang="en">
<head>
<meta charset="utf-8">
<title>MP Frameworks — Business Card</title>
<link href="https://fonts.googleapis.com/css2?family=Jost:wght@400;600&family=Open+Sans:wght@400&display=swap" rel="stylesheet">
<style>
  :root {
    --backdrop: #4b4e50;
    --card-dark: #000000;
    --card-light: #ffffff;
    --ink-light: #ffffff;
    --ink-dark: #1f1f1f;
    --card-shadow: 0 6px 14px rgba(0,0,0,0.45);
  }
  html, body {
    margin: 0;
    padding: 0;
    width: 1200px;
    height: 1000px;
    overflow: hidden;
    background: var(--backdrop);
  }
  .canvas {
    position: relative;
    width: 1200px;
    height: 1000px;
  }
  .card {
    position: absolute;
    width: 715px;
    height: 408px;
    box-shadow: var(--card-shadow);
  }
  .card--front {
    left: 120px;
    top: 75px;
    background: var(--card-dark);
  }
  .card--back {
    left: 379px;
    top: 522px;
    background: var(--card-light);
  }
  .brand {
    position: absolute;
    display: flex;
    align-items: center;
    gap: 14px;
    font-family: "Jost", sans-serif;
    font-weight: 400;
    letter-spacing: 0.06em;
    line-height: 1.05;
  }
  .brand__dot {
    border-radius: 50%;
    flex: none;
  }
  .card--front .brand {
    left: 225px;
    top: 148px;
    color: var(--ink-light);
    font-size: 36px;
  }
  .card--front .brand__dot {
    width: 22px;
    height: 22px;
    background: var(--ink-light);
  }
  .card--back .brand {
    left: 92px;
    top: 164px;
    color: var(--ink-dark);
    font-size: 25px;
  }
  .card--back .brand__dot {
    width: 15px;
    height: 15px;
    background: var(--ink-dark);
  }
  .holder-name {
    position: absolute;
    left: 383px;
    top: 66px;
    margin: 0;
    font-family: "Jost", sans-serif;
    font-weight: 600;
    font-size: 19px;
    letter-spacing: 0.28em;
    color: var(--ink-dark);
    text-transform: uppercase;
  }
  .contact {
    position: absolute;
    left: 380px;
    top: 230px;
    margin: 0;
    padding: 0;
    list-style: none;
    font-family: "Open Sans", sans-serif;
    font-size: 21px;
    color: var(--ink-dark);
  }
  .contact__item {
    display: flex;
    align-items: center;
    gap: 10px;
    height: 38px;
  }
  .contact__icon {
    width: 20px;
    height: 20px;
    flex: none;
    fill: var(--ink-dark);
  }
</style>
</head>
<body>
<main class="canvas">
  <section class="card card--front" aria-label="Card front">
    <div class="brand">
      <span class="brand__dot"></span>
      <span class="brand__name">MP<br>FRAMEWORKS</span>
    </div>
  </section>

  <section class="card card--back" aria-label="Card back">
    <div class="brand">
      <span class="brand__dot"></span>
      <span class="brand__name">MP<br>FRAMEWORKS</span>
    </div>

    <h1 class="holder-name">Miles Perrow</h1>

    <ul class="contact">
      <li class="contact__item">
        <svg class="contact__icon" viewBox="0 0 24 24" aria-hidden="true"><path d="M6.6 10.8a15.1 15.1 0 0 0 6.6 6.6l2.2-2.2c.3-.3.7-.4 1-.2 1.1.4 2.3.6 3.6.6.6 0 1 .4 1 1V20c0 .6-.4 1-1 1A17 17 0 0 1 3 4c0-.6.4-1 1-1h3.5c.6 0 1 .4 1 1 0 1.3.2 2.5.6 3.6.1.3 0 .7-.2 1z"/></svg>
        <span>07812 593174</span>
      </li>
      <li class="contact__item">
        <svg class="contact__icon" viewBox="0 0 24 24" aria-hidden="true"><path d="M2 5h20v14H2z M3.5 6.5 12 13l8.5-6.5" fill="none" stroke="#1f1f1f" stroke-width="0"/><path d="M2 5h20v1.2l-10 7-10-7z"/><path d="M2 8l10 7 10-7v11H2z"/></svg>
        <span>miles@mpframeworks.co.uk</span>
      </li>
      <li class="contact__item">
        <svg class="contact__icon" viewBox="0 0 24 24" aria-hidden="true"><g fill="none" stroke="#1f1f1f" stroke-width="1.8"><circle cx="12" cy="12" r="9.5"/><ellipse cx="12" cy="12" rx="4.2" ry="9.5"/><path d="M2.5 12h19M4 7h16M4 17h16"/></g></svg>
        <span>mpframeworks.co.uk</span>
      </li>
    </ul>
  </section>
</main>
</body>
</html>
```